Hall of Fame annnouncement graphic for social media

I need a social media Hall of Fame announcement designed in the styles of some of the examples I've posted. I have attached the two gentlemens head shots ... the names are Dale Prosser and Jim Harnden

It is for the BRIARWOOD LINKS HONOR SOCIETY also include 2026 Inductees ... I have also attached the logo... make the post in similar colors as the logo.

I need this tomorrow so I am going to pick a winner in the next 24 hours.

```html
<!DOCTYPE html>
<html lang="en">
<head>
<meta charset="utf-8">
<title>Briarwood Links Honor Society – 2026 Inductees</title>
<link href="https://fonts.googleapis.com/css2?family=Figtree:wght@400;800&display=swap" rel="stylesheet">
<style>
  :root {
    --page: #bdbdbf;
    --navy: #1f344c;
    --white: #ffffff;
    --gold: #f6c327;
    --blue: #0277c2;
    --photo-warm: #d9c7b8;
    --photo-cool: #b7c8b4;
  }
  * { margin: 0; padding: 0; box-sizing: border-box; }
  html, body {
    width: 1200px;
    height: 612px;
    overflow: hidden;
    background: var(--page);
    font-family: "Figtree", sans-serif;
  }
  .announcement {
    position: absolute;
    left: 72px;
    top: 71px;
    width: 1060px;
    height: 471px;
    background: var(--navy);
  }
  .society-name {
    position: absolute;
    left: 52px;
    top: 150px;
    width: 500px;
    text-align: center;
    color: var(--white);
    font-weight: 800;
    font-size: 40px;
    line-height: 1.1;
    letter-spacing: 1px;
  }
  .inductee-year {
    position: absolute;
    left: 52px;
    top: 312px;
    width: 500px;
    text-align: center;
    color: var(--gold);
    font-weight: 400;
    font-size: 29px;
  }
  .inductee {
    position: absolute;
    top: 85px;
    width: 206px;
  }
  .inductee--first { left: 598px; }
  .inductee--second { left: 827px; }
  .headshot {
    display: block;
    margin-left: 20px;
    width: 163px;
    height: 198px;
    border-bottom-right-radius: 18px;
  }
  .headshot--warm { background: linear-gradient(160deg, #ece4da 0%, var(--photo-warm) 55%, #f1f1f1 100%); }
  .headshot--outdoor { background: linear-gradient(180deg, #dfe7ee 0%, #cfd9dd 40%, var(--photo-cool) 60%, #eeeef2 100%); }
  .name-bar {
    height: 54px;
    background: var(--blue);
    color: var(--white);
    font-weight: 800;
    font-size: 30px;
    line-height: 54px;
    text-align: center;
    white-space: nowrap;
  }
</style>
</head>
<body>
  <section class="announcement">
    <h1 class="society-name">BRIARWOOD LINKS<br>HONOR SOCIETY</h1>
    <p class="inductee-year">2026 Inductees</p>

    <figure class="inductee inductee--first">
      <div class="headshot headshot--warm" role="img" aria-label="Headshot of Dale Prosser, smiling, in a white polo shirt"></div>
      <figcaption class="name-bar">Dale Prosser</figcaption>
    </figure>

    <figure class="inductee inductee--second">
      <div class="headshot headshot--outdoor" role="img" aria-label="Photo of Jim Harnden in a white polo shirt on a golf course"></div>
      <figcaption class="name-bar">Jim Harnden</figcaption>
    </figure>
  </section>
</body>
</html>
```